Salsa Company Needs New Label Design

Brookvale Food Company is company launching its second product line — La Fogata Rojo Salsa. We need a label that closely emulates the attached La Fogata All-Natural Salsa label for layout inspiration and follows our existing color and brand guidelines as described in the attached Word document.

```html
<!DOCTYPE html>
<html lang="en">
<head>
<meta charset="utf-8">
<title>La Fogata Rojo Hot Salsa Label</title>
<link rel="stylesheet" href="https://fonts.googleapis.com/css2?family=Alfa+Slab+One&family=Oswald:wght@500&display=swap">
<style>
  :root {
    --red: #c91d2b;
    --red-light: #e0404f;
    --red-deep: #a8151f;
    --gold: #f6a726;
    --gold-light: #fbd15f;
    --ink: #1c1c1c;
    --white: #ffffff;
    --page: #ffffff;
  }
  html, body {
    margin: 0;
    width: 1200px;
    height: 1200px;
    overflow: hidden;
    background: var(--page);
  }
  .label {
    position: absolute;
    left: 130px;
    top: 120px;
    width: 940px;
    height: 960px;
    background: radial-gradient(ellipse at 50% 45%, var(--red-light) 0%, var(--red) 45%, var(--red-deep) 100%);
    overflow: hidden;
  }
  .band {
    position: absolute;
    left: 0;
    width: 100%;
    height: 30px;
    background: linear-gradient(180deg, var(--gold) 0%, var(--gold-light) 50%, var(--gold) 100%);
  }
  .band--top { top: 0; }
  .band--bottom { bottom: 0; }
  .band::after {
    content: "";
    position: absolute;
    left: 0; right: 0;
    height: 3px;
    background: var(--red-deep);
  }
  .band--top::after { bottom: 6px; }
  .band--bottom::after { top: 6px; }
  .glow {
    position: absolute;
    left: 120px;
    top: 110px;
    width: 700px;
    height: 420px;
    border-radius: 50%;
    background: radial-gradient(ellipse at center, rgba(255,120,130,0.35) 0%, rgba(255,120,130,0) 70%);
  }
  .brand {
    position: absolute;
    left: 0;
    width: 100%;
    top: 150px;
    text-align: center;
    font-family: "Alfa Slab One", serif;
    font-size: 150px;
    line-height: 1;
    color: var(--gold);
    margin: 0;
  }
  .panel {
    position: absolute;
    left: 0;
    top: 0;
  }
  .product-name {
    position: absolute;
    left: 0;
    width: 100%;
    top: 532px;
    text-align: center;
    font-family: "Alfa Slab One", serif;
    font-size: 78px;
    line-height: 1;
    color: var(--white);
    margin: 0;
    letter-spacing: 1px;
  }
  .product-type {
    position: absolute;
    left: 0;
    width: 100%;
    top: 655px;
    text-align: center;
    font-family: "Alfa Slab One", serif;
    font-size: 76px;
    line-height: 1;
    color: var(--red);
    margin: 0;
  }
  .tagline {
    position: absolute;
    left: 0;
    width: 100%;
    top: 748px;
    text-align: center;
    font-family: "Oswald", sans-serif;
    font-weight: 500;
    font-size: 28px;
    color: var(--ink);
    margin: 0;
  }
  .net-weight {
    position: absolute;
    left: 178px;
    top: 862px;
    font-family: "Oswald", sans-serif;
    font-weight: 500;
    font-size: 28px;
    color: var(--white);
    margin: 0;
  }
  .heat-level {
    position: absolute;
    left: 640px;
    top: 850px;
    font-family: "Alfa Slab One", serif;
    font-size: 52px;
    line-height: 1;
    color: var(--white);
    margin: 0;
  }
</style>
</head>
<body>
  <main class="label">
    <div class="band band--top"></div>
    <div class="glow" role="img" aria-label="Sunburst rays radiating behind the brand name"></div>

    <h1 class="brand">La Fogata</h1>

    <svg class="panel" width="940" height="960" viewBox="0 0 940 960" aria-hidden="true">
      <defs>
        <linearGradient id="plaqueFill" x1="0" y1="0" x2="1" y2="0">
          <stop offset="0" stop-color="#f6a726"/>
          <stop offset="0.5" stop-color="#fbd15f"/>
          <stop offset="1" stop-color="#f6a726"/>
        </linearGradient>
      </defs>
      <!-- peaked plaque -->
      <path d="M180 600 L470 500 L760 600 L760 830 L180 830 Z" fill="url(#plaqueFill)" stroke="#f6a726" stroke-width="4"/>
      <path d="M196 612 L470 520 L744 612 L744 814 L196 814 Z" fill="none" stroke="#c91d2b" stroke-width="3"/>
      <!-- ribbon -->
      <path d="M150 520 L790 520 L760 580 L790 640 L150 640 L180 580 Z" fill="#1c1c1c"/>
      <path d="M164 528 L776 528 L750 580 L776 632 L164 632 L190 580 Z" fill="none" stroke="#ffffff" stroke-opacity="0.25" stroke-width="2"/>
    </svg>

    <h2 class="product-name">ROJO HOT</h2>
    <p class="product-type">SALSA</p>
    <p class="tagline">AUTHENTIC FLAVOR | SMALL BATCH CRAFTED</p>

    <p class="net-weight">NT WT 16OZ (454g)</p>
    <p class="heat-level">HOT</p>

    <div class="band band--bottom"></div>
  </main>
</body>
</html>
```